Management Company Needs Web Banners

We need a new set of bidkite banners developed. Here is what we would like to have:

1. Connect the branding with tangram images from www.VelarShifts.com
2. Have a "Call to Action" like a "LET'S TALK" Button

1. 728x90 Investments Need Expert Management.
2. 300x250 Senior Living Turnaround Experts
3. 728x90 MERQA Finds Lost Revenue in Senior Living Investments
4. 600x315 Senior Living Turnaround Experts

Target Market(s)

Private Equity, Health Care REITs, physicians, pharmacist, etc.

Industry/Entity Type

Management Consulting

Requirements
Must have
• A branding connection to https://www.VelarShifts.com/

```html
<!DOCTYPE html>
<html lang="en">
<head>
<meta charset="utf-8">
<title>MERQA Web Banners</title>
<link href="https://fonts.googleapis.com/css2?family=Poppins:wght@600&display=swap" rel="stylesheet">
<style>
  :root {
    --canvas: #f0f0f0;
    --banner-dark: #33261d;
    --banner-mid: #45352a;
    --banner-warm: #4d3322;
    --text-light: #ffffff;
    --accent-gold: #c79d6f;
    --mark-grey: #b5b5b5;
  }
  * { margin: 0; padding: 0; box-sizing: border-box; }
  html, body {
    width: 1200px; height: 692px; overflow: hidden;
    background: var(--canvas);
    font-family: "Poppins", "Century Gothic", sans-serif;
    font-weight: 600;
  }
  .canvas { position: relative; width: 1200px; height: 692px; }
  .banner { position: absolute; overflow: hidden; color: var(--text-light); }
  .banner-bg {
    position: absolute; inset: 0;
    background:
      radial-gradient(ellipse at 30% 70%, var(--banner-warm) 0%, transparent 55%),
      radial-gradient(ellipse at 75% 30%, var(--banner-mid) 0%, transparent 60%),
      var(--banner-dark);
  }
  .banner-content { position: absolute; inset: 0; }
  .accent { color: var(--accent-gold); }

  .brand { display: flex; align-items: center; justify-content: center; gap: 10px; }
  .brand-dot { border-radius: 50%; background: var(--mark-grey); flex: none; }
  .brand-name { color: var(--text-light); letter-spacing: 0.5px; line-height: 1; }

  .cta {
    position: absolute; display: flex; align-items: center; justify-content: center;
    border: 3px solid var(--accent-gold); color: var(--text-light); line-height: 1;
  }

  /* 300x250 */
  .banner-rect { left: 45px; top: 58px; width: 292px; height: 244px; }
  .banner-rect .brand { position: absolute; top: 17px; left: 0; right: 0; }
  .banner-rect .brand-dot { width: 56px; height: 56px; }
  .banner-rect .brand-name { font-size: 34px; }
  .banner-rect .headline {
    position: absolute; top: 86px; left: 0; right: 0; text-align: center;
    font-size: 23px; line-height: 31px;
  }
  .banner-rect .cta { left: 85px; top: 191px; width: 120px; height: 35px; font-size: 17px; }

  /* 728x90 leaderboards */
  .banner-leader { left: 375px; width: 708px; height: 88px; }
  .banner-leader.first { top: 79px; }
  .banner-leader.second { top: 194px; }
  .banner-leader .brand-dot {
    position: absolute; left: 22px; top: 8px; width: 72px; height: 72px;
    border-radius: 50%; background: var(--mark-grey);
  }
  .banner-leader .headline {
    position: absolute; left: 150px; width: 344px; top: 12px; text-align: center;
    font-size: 23px; line-height: 32px; white-space: nowrap;
  }
  .banner-leader .cta { left: 547px; top: 28px; width: 129px; height: 38px; font-size: 18px; }

  /* 600x315 */
  .banner-social { left: 297px; top: 344px; width: 584px; height: 306px; }
  .banner-social .brand { position: absolute; top: 22px; left: 0; right: 0; }
  .banner-social .brand-dot { width: 54px; height: 54px; }
  .banner-social .brand-name { font-size: 40px; }
  .banner-social .headline {
    position: absolute; top: 102px; left: 0; right: 0; text-align: center;
    font-size: 40px; line-height: 52px;
  }
  .banner-social .cta { left: 201px; top: 228px; width: 192px; height: 57px; font-size: 29px; }
</style>
</head>
<body>
<main class="canvas">

  <section class="banner banner-rect">
    <div class="banner-bg" role="img" aria-label="Dimmed photo of wooden tangram pieces on a table"></div>
    <div class="banner-content">
      <div class="brand"><span class="brand-dot"></span><span class="brand-name">MERQA</span></div>
      <h2 class="headline">Senior Living<br><span class="accent">Turnaround<br>Experts</span></h2>
      <a class="cta">Let’s Talk</a>
    </div>
  </section>

  <section class="banner banner-leader first">
    <div class="banner-bg" role="img" aria-label="Dimmed photo of wooden tangram pieces on a table"></div>
    <div class="banner-content">
      <span class="brand-dot"></span>
      <h2 class="headline">Investments Need <span class="accent">Expert<br>Management</span></h2>
      <a class="cta">Let’s Talk</a>
    </div>
  </section>

  <section class="banner banner-leader second">
    <div class="banner-bg" role="img" aria-label="Dimmed photo of wooden tangram pieces on a table"></div>
    <div class="banner-content">
      <span class="brand-dot"></span>
      <h2 class="headline">MERQA Finds Lost Revenue<br>in <span class="accent">Senior Living Investments</span></h2>
      <a class="cta">Let’s Talk</a>
    </div>
  </section>

  <section class="banner banner-social">
    <div class="banner-bg" role="img" aria-label="Dimmed photo of wooden tangram pieces on a table"></div>
    <div class="banner-content">
      <div class="brand"><span class="brand-dot"></span><span class="brand-name">MERQA</span></div>
      <h2 class="headline">Senior Living<br><span class="accent">Turnaround Experts</span></h2>
      <a class="cta">Let’s Talk</a>
    </div>
  </section>

</main>
</body>
</html>
```